Children's book business card contest - The more bright colors the better

Hello

PLEASE incorporate THE CHARACTERS ILLUSTRATIONS on the most recent uploaded attachment on the business card.

I'm in the process of completing my first manuscript for my children's book series TiKi TELLS a series of stories from a blended family.

My illustrator and I just completed our logo which you will find attached. Additionally you will find my first idea for my business card which I took from Cardwellio just says it means to get started but I really like the color schema. I will be getting my business card out to editors, agents, teachers, and anyone in the children's book realm. The card needs to be bright, friendly and inviting. It needs to remind you of children I do want a double sided card but I am very open as far as design layout. Below is a description of the book series and how the series will go to give you motivation or ideas. Please only submit injuries worthy of national recognition as the business cards will be passed out across the country to some of the top writing professionals in the industry at a childrens writing conference I will be attending.

Like I mentioned previously please review the information below as it gives you background too much children's book series. I look forward to working with my designer and I look forward to the submissions.

"I'm looking for someone with experience in illustrating children's books and is also passionate about this specific illustration type. My book series will be a series of short stories from a blended family. Each book well always have the same characters but the storyline will be different. Additionally, I'm looking for someone who has experience in taking real life photos and creating real like cartoon illustrations. My children's book series idea is based off of my family and I want us to be the characters. Also, if you have a writing background and could help me with editing that would be a very big plus as well. One of the niches for my children's book series is that my blended family is also blended because of ethnicity. My children's book series will bring light to multiculturalism in families and the different diversities blended families go through. This is an untapped industry in the children's book market. If you have experience with grant writing I am very interested in that as well. Please feel free to respond to any of my needs that you feel you are applicable for. I know I've created an idea that will revolutionize how parents and children read and learn together. My book series idea is innovative, fun and has tremendous crossover ability. Please only reply if you are seriously interested and have current availability. I'm ready to be GREAT and I hope you don't pass on the opportunity to join me! "

Please note: I will be using Cardwellio for my business card ordering so please constructive business card to fit those parameters. Additionally there are three attachments I provided one of them is the actual logo, the other is the almost completed book cover, and the other one is my current business cards from Cardwellio that I am looking to replace.

Target Market(s)

Children and Writing Professionals

Industry/Entity Type

Business

Contact Information for Business Card

I would like this business card to be very colorful. The card needs to attract business writing professionals as well as appeal to children and teachers inside the schooling network

Font styles to use
Serif
Sans Serif

Requirements
Must have
• A lot of color, characteristic, informative and must have all of my contact information
Nice to have
• Originality

```html
<!DOCTYPE html>
<html lang="en">
<head>
<meta charset="UTF-8">
<title>TiKi TELLS – Business Card</title>
<link rel="stylesheet" href="https://fonts.googleapis.com/css2?family=Comic+Neue:wght@400;700&display=swap">
<style>
  :root {
    --page-bg: #e9e7e3;
    --card-bg: #ffffff;
    --ink: #5a5a5a;
    --red: #e3262b;
    --green: #3a9b2e;
    --blue: #2a6fd1;
    --purple: #7b3fc4;
    --yellow: #f4d216;
    --magenta: #d43cc4;
    --art-light: #dfe3f2;
    --art-mid: #6f7fc8;
    --art-deep: #4a3f9a;
  }
  * { box-sizing: border-box; margin: 0; padding: 0; }
  html, body {
    width: 1200px;
    height: 950px;
    overflow: hidden;
    background: var(--page-bg);
    font-family: "Comic Neue", "Comic Sans MS", sans-serif;
  }
  .card {
    position: absolute;
    left: 75px;
    top: 175px;
    width: 1050px;
    height: 600px;
    background: var(--card-bg);
    box-shadow: 0 10px 30px rgba(0,0,0,0.18);
    overflow: hidden;
  }
  .family-art {
    position: absolute;
    right: 40px;
    top: 40px;
    width: 470px;
    height: 400px;
    border-radius: 18px;
    background: radial-gradient(ellipse at 50% 55%, var(--art-mid) 0%, var(--art-light) 70%, var(--card-bg) 100%);
  }
  .brand {
    position: absolute;
    left: 70px;
    top: 150px;
  }
  .brand-name {
    font-size: 92px;
    font-weight: 700;
    line-height: 1;
    color: var(--red);
    letter-spacing: 2px;
  }
  .person {
    position: absolute;
    left: 80px;
    top: 280px;
  }
  .person-name {
    font-size: 40px;
    font-weight: 400;
    color: var(--red);
    line-height: 1.1;
  }
  .person-role {
    font-size: 32px;
    color: var(--green);
    margin-top: 4px;
  }
  .contacts {
    position: absolute;
    left: 80px;
    top: 390px;
    list-style: none;
  }
  .contact {
    display: flex;
    align-items: center;
    gap: 12px;
    font-size: 25px;
    color: var(--ink);
    height: 38px;
  }
  .contact-dot {
    width: 24px;
    height: 24px;
    border-radius: 50%;
    display: flex;
    align-items: center;
    justify-content: center;
    flex: none;
  }
  .dot-phone { background: var(--blue); }
  .dot-mail { background: var(--purple); }
  .dot-web { background: var(--yellow); }
  .dot-social { background: var(--magenta); }
  .edge-stripes {
    position: absolute;
    left: 0;
    bottom: 0;
    width: 100%;
    height: 24px;
    display: flex;
  }
  .edge-stripes span { flex: 1; }
  .s-red { background: var(--red); }
  .s-green { background: var(--green); }
  .s-blue { background: var(--blue); }
  .s-purple { background: var(--purple); }
  .s-yellow { background: var(--yellow); }
  .s-magenta { background: var(--magenta); }
</style>
</head>
<body>
  <main class="card">
    <div class="family-art" role="img" aria-label="Illustration of the author's blended family of characters with their dog"></div>

    <div class="brand">
      <div class="brand-name">TiKi TELLS</div>
    </div>

    <div class="person">
      <div class="person-name">Talia Morgan</div>
      <div class="person-role">Author/Founder</div>
    </div>

    <ul class="contacts">
      <li class="contact">
        <span class="contact-dot dot-phone">
          <svg width="14" height="14" viewBox="0 0 24 24" aria-hidden="true">
            <path fill="#fff" d="M6.6 10.8a15.1 15.1 0 0 0 6.6 6.6l2.2-2.2c.3-.3.7-.4 1-.2 1.1.4 2.3.6 3.6.6.6 0 1 .4 1 1V20c0 .6-.4 1-1 1A17 17 0 0 1 3 4c0-.6.4-1 1-1h3.5c.6 0 1 .4 1 1 0 1.3.2 2.5.6 3.6.1.3 0 .7-.2 1z"/>
          </svg>
        </span>
        555.214.0737
      </li>
      <li class="contact">
        <span class="contact-dot dot-mail">
          <svg width="14" height="14" viewBox="0 0 24 24" aria-hidden="true">
            <rect x="3" y="6" width="18" height="12" rx="1" fill="none" stroke="#fff" stroke-width="2"/>
            <path d="M3 7l9 6 9-6" fill="none" stroke="#fff" stroke-width="2"/>
          </svg>
        </span>
        Talia@tikitells.xyz
      </li>
      <li class="contact">
        <span class="contact-dot dot-web">
          <svg width="14" height="14" viewBox="0 0 24 24" aria-hidden="true">
            <circle cx="12" cy="12" r="8" fill="none" stroke="#fff" stroke-width="2"/>
            <path d="M4 12h16M12 4c3 3 3 13 0 16M12 4c-3 3-3 13 0 16" fill="none" stroke="#fff" stroke-width="1.5"/>
          </svg>
        </span>
        www.tikitells.xyz
      </li>
      <li class="contact">
        <span class="contact-dot dot-social"></span>
        @tiki_tells_xyz
      </li>
    </ul>

    <div class="edge-stripes" aria-hidden="true">
      <span class="s-red"></span>
      <span class="s-green"></span>
      <span class="s-blue"></span>
      <span class="s-purple"></span>
      <span class="s-yellow"></span>
      <span class="s-magenta"></span>
    </div>
  </main>
</body>
</html>
```